need 4 creative A frame (SANDWICH BOARD) designs concepts for dental office

need 4 creative A frame (SANDWICH BOARD) designs concepts
1 - targeting kids
2. targeting old age
3. targeting teens
4 targeting general public

website - www.pinecrestdental.ca

LINK for Measurements for sandwich board https://www.vordex.ca/KQ_4837/Steel-Clip-Rim-Folding-Board

i am attaching certain key ingredients ( rough sketch in uploaded files ) to be added on each design though not mandatory if the design is very creative

```html
<!DOCTYPE html>
<html lang="en">
<head>
<meta charset="utf-8">
<title>Pinecrest Dental – A-Frame Sign Concepts</title>
<link href="https://fonts.googleapis.com/css2?family=Montserrat:wght@600;700;800&display=swap" rel="stylesheet">
<style>
  :root {
    --navy: #17234a;
    --orange: #ef5a2a;
    --sky: #08b1e8;
    --sky-pale: #e4f5fc;
    --grey: #8a8d92;
    --white: #ffffff;
  }
  * { margin: 0; padding: 0; box-sizing: border-box; }
  html, body { width: 907px; height: 1200px; overflow: hidden; background: var(--white); }
  body { position: relative; font-family: "Montserrat", Arial, sans-serif; }

  .sign {
    position: absolute; width: 264px; height: 336px;
    background: var(--white); overflow: hidden;
    box-shadow: 0 1px 4px rgba(0,0,0,0.25);
  }
  .col-1 { left: 23px; } .col-2 { left: 320px; } .col-3 { left: 619px; }
  .row-1 { top: 36px; } .row-2 { top: 431px; } .row-3 { top: 828px; }

  .sign__photo { position: absolute; left: 0; top: 0; width: 264px; height: 145px; }
  .photo--kids { background: linear-gradient(180deg, #ffffff 0%, #fbfbfb 45%, #e9c9a8 60%, #d23b3f 80%, #f1b640 100%); }
  .photo--seniors { background: linear-gradient(120deg, #cfc6b8 0%, #e4ddd2 40%, #9ea2a6 75%, #6f6f70 100%); }
  .photo--family { background: linear-gradient(180deg, #7da267 0%, #c8d7b8 35%, #e9c3a9 60%, #e6e3de 100%); }

  .sign__tagline {
    position: absolute; left: 0; right: 0; top: 12px;
    text-align: center; font-weight: 700; font-size: 14px;
    color: var(--navy); letter-spacing: 0.2px;
  }
  .sign__rule { position: absolute; left: 0; right: 0; top: 149px; height: 2px; background: var(--sky); }

  .sign__badge {
    position: absolute; left: 198px; top: 133px; width: 50px; height: 50px;
    border-radius: 50%; background: var(--sky);
    border: 2px dashed var(--white); outline: 2px solid var(--sky);
    color: var(--white); text-align: center; font-weight: 800; line-height: 1;
    display: flex; flex-direction: column; align-items: center; justify-content: center;
  }
  .sign__badge .small { font-size: 7px; }
  .sign__badge .big { font-size: 20px; color: var(--navy); -webkit-text-stroke: 0.5px var(--white); }

  .sign__brand {
    position: absolute; left: 0; right: 0; top: 162px;
    text-align: center; font-weight: 600; font-size: 24px; color: var(--grey);
  }
  .sign__name {
    position: absolute; left: 0; right: 0; top: 193px;
    text-align: center; font-weight: 800; font-size: 42px; color: var(--orange);
    letter-spacing: 2px; line-height: 1;
  }
  .sign__arrows { position: absolute; left: 0; top: 235px; width: 264px; height: 44px; }
  .sign__cta {
    position: absolute; left: 0; right: 0; top: 281px;
    text-align: center; font-weight: 700; font-size: 16px; color: var(--navy);
  }
  .sign__phone {
    position: absolute; left: 0; right: 0; bottom: 0; height: 33px;
    background: var(--sky); color: var(--navy);
    display: flex; align-items: center; justify-content: center; gap: 7px;
    font-weight: 800; font-size: 24px; letter-spacing: 1px;
  }
  .sign__phone svg { width: 17px; height: 17px; }
</style>
</head>
<body>
<svg width="0" height="0" style="position:absolute">
  <defs>
    <symbol id="chevrons-left" viewBox="0 0 264 44">
      <g fill="var(--sky-pale)">
        <polygon points="52,0 68,0 46,22 68,44 52,44 30,22"/>
        <polygon points="82,0 98,0 76,22 98,44 82,44 60,22"/>
        <polygon points="166,0 182,0 160,22 182,44 166,44 144,22"/>
        <polygon points="196,0 212,0 190,22 212,44 196,44 174,22"/>
        <polygon points="226,0 242,0 220,22 242,44 226,44 204,22"/>
      </g>
      <g fill="var(--sky)">
        <polygon points="110,0 128,0 106,22 128,44 110,44 88,22"/>
        <polygon points="142,0 160,0 138,22 160,44 142,44 120,22"/>
      </g>
    </symbol>
    <symbol id="phone-icon" viewBox="0 0 24 24">
      <path fill="var(--navy)" d="M6.6 10.8c1.4 2.8 3.8 5.1 6.6 6.6l2.2-2.2c.3-.3.7-.4 1-.2 1.1.4 2.3.6 3.6.6.6 0 1 .4 1 1V20c0 .6-.4 1-1 1C10.6 21 3 13.4 3 4c0-.6.4-1 1-1h3.5c.6 0 1 .4 1 1 0 1.3.2 2.5.6 3.6.1.3 0 .7-.2 1L6.6 10.8z"/>
    </symbol>
  </defs>
</svg>

<!-- Row 1: left arrows -->
<section class="sign col-1 row-1">
  <div class="sign__photo photo--kids" role="img" aria-label="Group of smiling children with playful butterflies"></div>
  <div class="sign__tagline">WE LOVE KIDS</div>
  <div class="sign__rule"></div>
  <div class="sign__brand">Pinecrest</div>
  <div class="sign__badge"><span class="small">OPEN</span><span class="big">7</span><span class="small">DAYS</span></div>
  <div class="sign__name">DENTAL</div>
  <svg class="sign__arrows"><use href="#chevrons-left"/></svg>
  <div class="sign__cta">Accepting New Patients</div>
  <div class="sign__phone"><svg><use href="#phone-icon"/></svg>555 014 2876</div>
</section>
<section class="sign col-2 row-1">
  <div class="sign__photo photo--seniors" role="img" aria-label="Smiling senior couple chatting in a lounge"></div>
  <div class="sign__tagline">WE CARE YOUNG HEARTS</div>
  <div class="sign__rule"></div>
  <div class="sign__brand">Pinecrest</div>
  <div class="sign__badge"><span class="small">OPEN</span><span class="big">7</span><span class="small">DAYS</span></div>
  <div class="sign__name">DENTAL</div>
  <svg class="sign__arrows"><use href="#chevrons-left"/></svg>
  <div class="sign__cta">Accepting New Patients</div>
  <div class="sign__phone"><svg><use href="#phone-icon"/></svg>555 014 2876</div>
</section>
<section class="sign col-3 row-1">
  <div class="sign__photo photo--family" role="img" aria-label="Three-generation family sitting together on a sofa"></div>
  <div class="sign__tagline">WE CARE YOUR LOVED ONES</div>
  <div class="sign__rule"></div>
  <div class="sign__brand">Pinecrest</div>
  <div class="sign__badge"><span class="small">OPEN</span><span class="big">7</span><span class="small">DAYS</span></div>
  <div class="sign__name">DENTAL</div>
  <svg class="sign__arrows"><use href="#chevrons-left"/></svg>
  <div class="sign__cta">Accepting New Patients</div>
  <div class="sign__phone"><svg><use href="#phone-icon"/></svg>555 014 2876</div>
</section>

<!-- Row 2: right arrows -->
<section class="sign col-1 row-2">
  <div class="sign__photo photo--kids" role="img" aria-label="Group of smiling children with playful butterflies"></div>
  <div class="sign__tagline">WE LOVE KIDS</div>
  <div class="sign__rule"></div>
  <div class="sign__brand">Pinecrest</div>
  <div class="sign__badge"><span class="small">OPEN</span><span class="big">7</span><span class="small">DAYS</span></div>
  <div class="sign__name">DENTAL</div>
  <svg class="sign__arrows" style="transform:scaleX(-1)"><use href="#chevrons-left"/></svg>
  <div class="sign__cta">Accepting New Patients</div>
  <div class="sign__phone"><svg><use href="#phone-icon"/></svg>555 014 2876</div>
</section>
<section class="sign col-2 row-2">
  <div class="sign__photo photo--seniors" role="img" aria-label="Smiling senior couple chatting in a lounge"></div>
  <div class="sign__tagline">WE CARE YOUNG HEARTS</div>
  <div class="sign__rule"></div>
  <div class="sign__brand">Pinecrest</div>
  <div class="sign__badge"><span class="small">OPEN</span><span class="big">7</span><span class="small">DAYS</span></div>
  <div class="sign__name">DENTAL</div>
  <svg class="sign__arrows" style="transform:scaleX(-1)"><use href="#chevrons-left"/></svg>
  <div class="sign__cta">Accepting New Patients</div>
  <div class="sign__phone"><svg><use href="#phone-icon"/></svg>555 014 2876</div>
</section>
<section class="sign col-3 row-2">
  <div class="sign__photo photo--family" role="img" aria-label="Three-generation family sitting together on a sofa"></div>
  <div class="sign__tagline">WE CARE YOUR LOVED ONES</div>
  <div class="sign__rule"></div>
  <div class="sign__brand">Pinecrest</div>
  <div class="sign__badge"><span class="small">OPEN</span><span class="big">7</span><span class="small">DAYS</span></div>
  <div class="sign__name">DENTAL</div>
  <svg class="sign__arrows" style="transform:scaleX(-1)"><use href="#chevrons-left"/></svg>
  <div class="sign__cta">Accepting New Patients</div>
  <div class="sign__phone"><svg><use href="#phone-icon"/></svg>555 014 2876</div>
</section>

<!-- Row 3: no arrows -->
<section class="sign col-1 row-3">
  <div class="sign__photo photo--kids" role="img" aria-label="Group of smiling children with playful butterflies"></div>
  <div class="sign__tagline">WE LOVE KIDS</div>
  <div class="sign__rule"></div>
  <div class="sign__brand">Pinecrest</div>
  <div class="sign__badge"><span class="small">OPEN</span><span class="big">7</span><span class="small">DAYS</span></div>
  <div class="sign__name">DENTAL</div>
  <div class="sign__cta">Accepting New Patients</div>
  <div class="sign__phone"><svg><use href="#phone-icon"/></svg>555 014 2876</div>
</section>
<section class="sign col-2 row-3">
  <div class="sign__photo photo--seniors" role="img" aria-label="Smiling senior couple chatting in a lounge"></div>
  <div class="sign__tagline">WE CARE YOUNG HEARTS</div>
  <div class="sign__rule"></div>
  <div class="sign__brand">Pinecrest</div>
  <div class="sign__badge"><span class="small">OPEN</span><span class="big">7</span><span class="small">DAYS</span></div>
  <div class="sign__name">DENTAL</div>
  <div class="sign__cta">Accepting New Patients</div>
  <div class="sign__phone"><svg><use href="#phone-icon"/></svg>555 014 2876</div>
</section>
<section class="sign col-3 row-3">
  <div class="sign__photo photo--family" role="img" aria-label="Three-generation family sitting together on a sofa"></div>
  <div class="sign__tagline">WE CARE YOUR LOVED ONES</div>
  <div class="sign__rule"></div>
  <div class="sign__brand">Pinecrest</div>
  <div class="sign__badge"><span class="small">OPEN</span><span class="big">7</span><span class="small">DAYS</span></div>
  <div class="sign__name">DENTAL</div>
  <div class="sign__cta">Accepting New Patients</div>
  <div class="sign__phone"><svg><use href="#phone-icon"/></svg>555 014 2876</div>
</section>
</body>
</html>
```